Flyer for New Spa Opening

We need a flyer to increase customer's awareness of our new spa located in Yangon, Myanmar, in a middle-upper class shopping mall. A new hotel will be opening above the mall in Dec 2013.
Updates

Have made payment guaranteed.  Need a good flyer. Thanks.

Hi, I have uploaded a Words File for Flyer Text. Thanks!

Dear Designers,

I have setup a 2nd award, there's too many outstanding designs! Thanks so much.

Regards
Marla

Target Market(s)

-Hotel guest who wants to a spa session to relax
-Woman between 18 - 55 years old who have high spending power in a poor country(Myanmar). They like to use "Big Brands" but do not have much variety available in their country.

Industry/Entity Type

Shopping

Requirements
Must have
• Our services include Body Spa, Facial, Nails, Waxing & Foot Reflexology. We use well-known international brands in our spa including Veridelle, KRU, Varnet, Brisola Terrano and MORLU.

Veridelle, the skin care system researched and developed by The Halvern Dermal Academy (HDA), is an international leader in today’s skin care industry.

We are authorized Veridelle skin spa to provide professional facial and retailing Veridelle products.

Include the logo of the brands

Willowmere Spa
add: No 72, Thuka Road, Min Ye Plaza (Level-5) (6187), Kyimyin Township, Yangon
tel: +959 47208613
email: contactus@velmora-unitedgroup.example

Nice to have
• visually nice and relaxing spa pictures.
Should not have
• price

```html
<!DOCTYPE html>
<html lang="en">
<head>
<meta charset="utf-8">
<title>Willowmere Spa – Tri-fold Brochure</title>
<link rel="stylesheet" href="https://fonts.googleapis.com/css2?family=Great+Vibes&family=Open+Sans:wght@300;400;600;700&display=swap">
<style>
:root{
  --page:#ece7e0;
  --wood-dark:#5e2414;
  --wood:#7c311b;
  --wood-light:#9a4526;
  --linen:#dccfbd;
  --linen-dark:#c8b9a4;
  --white:#ffffff;
  --pink:#d4336a;
  --grey:#6d6a66;
  --grey-light:#9a9690;
  --lime:#a8c83a;
  --band:#e9e2d8;
}
*{box-sizing:border-box;margin:0;padding:0}
html,body{width:1200px;height:1008px;overflow:hidden}
body{background:var(--page);font-family:"Open Sans",Arial,sans-serif;color:var(--grey);position:relative}
.spread{position:absolute;left:240px;width:720px;height:480px;display:flex;background:var(--linen);box-shadow:0 2px 8px rgba(0,0,0,.18)}
.spread--outside{top:12px}
.spread--inside{top:516px}
.panel{position:relative;width:240px;height:100%;overflow:hidden;background:var(--linen)}
.wood{background:linear-gradient(100deg,var(--wood-dark) 0%,var(--wood) 30%,var(--wood-light) 55%,var(--wood) 80%,var(--wood-dark) 100%)}
.box{position:absolute;left:8px;right:8px;background:var(--white)}
.photo{position:absolute;border-radius:4px}
.ornament{position:absolute;background:linear-gradient(135deg,var(--wood) 0%,var(--wood-light) 100%);border-radius:0 0 40px 0;opacity:.85}
.band{position:absolute;left:0;right:0;height:18px;background:linear-gradient(90deg,var(--band),#fff,var(--band));color:var(--grey);font-size:8.5px;letter-spacing:.4px;text-align:center;line-height:18px;text-transform:uppercase}
.band--wood{background:transparent;color:#f3e6d8}
.copy{font-size:6.6px;line-height:1.45;color:var(--grey);font-weight:400}
.headline{color:var(--pink);font-weight:300;font-size:12px;line-height:1.15}
.subhead{color:var(--pink);font-weight:600;font-size:8px;line-height:1.2;text-transform:uppercase}
.badge{position:absolute;width:54px;height:54px;border-radius:50%;background:radial-gradient(circle at 40% 35%,#c8e15c,var(--lime));color:#fff;font-size:5.4px;line-height:1.3;padding:12px 6px 0 9px;font-weight:600}
.badge ul{list-style:none}
.badge li::before{content:"• "}
.brand{font-weight:700;color:#fff;letter-spacing:.3px}
.brand--grey{color:var(--grey)}
.contact{font-size:6.8px;line-height:1.5;color:#f4e9dc;font-weight:600}
.title-script{font-family:"Great Vibes",cursive;color:var(--pink);font-size:38px;line-height:.95;text-align:center}
.tagline{font-size:10px;font-weight:300;color:var(--grey-light);text-align:center;line-height:1.25}
</style>
</head>
<body>

<!-- Outside spread -->
<section class="spread spread--outside">

  <article class="panel panel--facial">
    <div class="ornament" style="left:0;top:0;width:40px;height:44px" role="img" aria-label="Brown swirl ornament"></div>
    <h2 class="headline" style="position:absolute;left:48px;top:8px;right:8px">Our services include body spa, facial, nails, waxing &amp; foot reflexology</h2>
    <div class="band" style="top:60px">Facial</div>
    <div class="box" style="top:82px;height:112px;padding:6px">
      <p class="copy" style="width:120px">We are authorized Veridelle skin spa to provide Professional Facial and Retailing Veridelle products.</p>
      <div class="photo" style="right:6px;top:6px;width:80px;height:48px;background:linear-gradient(135deg,#f4f0ec,#d9c9bc)" role="img" aria-label="Skin care advertisement showing a smiling model"></div>
      <p style="margin-top:8px;font-weight:700;font-size:10px;color:var(--grey)">Veridelle</p>
      <p class="copy" style="margin-top:4px">Veridelle, the skin care system from US, researched and developed by The Halvern Dermal Academy (HDA), is an international leader in today's skin care industry.</p>
    </div>
    <div class="photo" style="left:8px;right:8px;top:200px;height:78px;background:linear-gradient(120deg,#f3e7df,#e2cfc3 60%,#c9b1a2)" role="img" aria-label="Woman receiving a facial mask treatment"></div>
    <div class="box" style="top:284px;bottom:8px;padding:6px">
      <h3 class="subhead">Chose from a customized facial or targeted treatment facial</h3>
      <div style="display:flex;gap:8px;margin-top:6px">
        <p class="copy" style="flex:1"><b>Customized Facial</b> is designed to address every client's skin type and concern. Our professionally trained therapists will carefully select the product and procedure that is most suitable for your skin to achieve true skin health.</p>
        <p class="copy" style="flex:1"><b>Targeted Treatment</b> includes LumaToneRX Facial, AgeWise Facial, CalmVeil Facial and PureClear Facial. Tell us your skin concern and we have the solution just for you!</p>
      </div>
    </div>
  </article>

  <article class="panel panel--foot">
    <div class="photo" style="left:8px;right:8px;top:10px;height:104px;background:linear-gradient(150deg,#e9c8b5,#b23a3a 65%,#5a1a14)" role="img" aria-label="Feet with red nails resting on rose petals"></div>
    <div class="band" style="top:120px">Foot Massage (1hr)</div>
    <div class="box" style="top:142px;height:78px;padding:6px">
      <p class="copy" style="width:150px">Pamper your feet that has taken you a hundred miles. Following a foot soak and cleansing, we will begin foot massage on your foot reflex zones stimulating body energy and on your muscles to soothe tired heavy legs.</p>
      <div class="badge" style="right:6px;top:12px"><ul><li>Includes:</li><li>Foot Soak</li><li>Foot Massage</li></ul></div>
    </div>
    <div class="wood" style="position:absolute;left:0;right:0;top:228px;bottom:0;padding:14px 14px">
      <p class="brand" style="font-size:14px;text-align:center">Veridelle</p>
      <div style="display:flex;justify-content:space-around;margin-top:10px;font-size:11px">
        <span class="brand">Varnet</span><span class="brand">KRU</span>
      </div>
      <div style="display:flex;justify-content:space-around;margin-top:8px;font-size:10px">
        <span class="brand">MORLU</span><span class="brand">Brisola Terrano</span>
      </div>
      <div class="contact" style="margin-top:40px">
        <p>Willowmere Spa</p>
        <p>No 72, Thuka Road, Min Ye Plaza (Level-5)</p>
        <p>(6187) - Kyimyin Township - Yangon</p>
        <p>Tel : +959 47208613</p>
        <p>email: contactus@velmora-unitedgroup.example</p>
      </div>
    </div>
  </article>

  <article class="panel panel--cover wood">
    <div class="box" style="top:14px;bottom:14px;left:10px;right:10px;padding:16px 10px 0">
      <div class="ornament" style="left:0;top:0;width:60px;height:30px" role="img" aria-label="Brown swirl ornament"></div>
      <h1 class="title-script" style="margin-top:22px">Willowmere<br>Spa</h1>
      <p class="tagline" style="margin-top:12px">A luxurious spa experience designed for total relaxation</p>
      <div class="photo" style="left:0;right:0;top:168px;height:160px;border-radius:0;background:linear-gradient(160deg,#f2d3c8,#e0577a 50%,#b82a45)" role="img" aria-label="Hands with red nails holding pink rose petals"></div>
      <p class="copy" style="position:absolute;left:10px;right:10px;top:336px;text-align:center;font-size:7px">We use well-known international brands in our spa.</p>
      <div style="position:absolute;left:10px;right:10px;top:356px;text-align:center;font-size:10px;line-height:1.7">
        <span class="brand brand--grey">Veridelle</span>
        <span class="brand brand--grey">&nbsp;Varnet</span><br>
        <span class="brand brand--grey">MORLU</span>
        <span class="brand brand--grey">&nbsp;KRU</span>
        <span class="brand brand--grey">&nbsp;Brisola Terrano</span>
      </div>
    </div>
  </article>
</section>

<!-- Inside spread -->
<section class="spread spread--inside">

  <article class="panel panel--nails wood">
    <div class="photo" style="left:0;right:0;top:0;height:62px;border-radius:0;background:linear-gradient(90deg,#f5eee9,#e8d9cf,#f3ebe5)" role="img" aria-label="Row of nail care bottles and creams"></div>
    <div class="band" style="top:68px">Nails</div>
    <div class="box" style="top:90px;height:108px;padding:6px">
      <p class="copy" style="width:118px">We know you love KRU! We have over 200 choices of KRU colours just for you. Our Nail Technicians are trained to provide the most meticulous Manicure &amp; Pedicure according to the Professional System by KRU.</p>
      <div class="photo" style="right:6px;top:6px;width:92px;height:52px;background:linear-gradient(135deg,#f0e3e6,#c25873)" role="img" aria-label="Decorated manicured nails"></div>
      <div class="photo" style="left:6px;bottom:6px;width:120px;height:26px;background:linear-gradient(90deg,#c0252e,#e04a3c,#b02030)" role="img" aria-label="Red nail polish bottles"></div>
    </div>
    <div class="band band--wood" style="top:202px">Body Spa</div>
    <div class="box" style="top:222px;height:226px">
      <div class="photo" style="left:0;top:0;width:130px;height:226px;border-radius:0;background:linear-gradient(160deg,#eef1e8,#cfdcc9 50%,#c98a4a)" role="img" aria-label="Body spa creams, oils and a brush"></div>
      <p class="copy" style="position:absolute;left:138px;top:20px;right:6px;font-size:7px">Indulge your body, mind and soul in one of our relaxing Spa Treatments.</p>
    </div>
    <div class="band band--wood" style="top:454px">Traditional Body Massage (1.5hrs)</div>
  </article>

  <article class="panel panel--dayspa wood">
    <div class="band band--wood" style="top:10px">Willowmere Day Spa (2.5hrs)</div>
    <div class="box" style="top:32px;height:130px;padding:6px">
      <p class="copy" style="width:130px">A luxurious spa experience designed for total relaxation. A delightful body scrub will leave your skin smooth to the touch, followed by a 60min Swedish Aromatherapy Massage. The treatment is complete with a body wrap to nourish your skin and your head gently massaged, giving you a profound sense of pleasure and well-being.</p>
      <div class="badge" style="right:8px;top:16px;width:62px;height:62px;padding-top:10px"><ul><li>Includes:</li><li>Body Scrub</li><li>60min Swedish Aromatherapy Massage</li><li>Body Wrap with Head Massage</li></ul></div>
    </div>
    <div class="band band--wood" style="top:172px;height:30px;line-height:13px;padding-top:2px">Swedish Aromatherapy<br>Body Massage (1.5hrs)</div>
    <div class="band band--wood" style="top:214px">Revitalizing Body Scrub (1hr)</div>
    <div class="box" style="top:236px;height:72px;padding:6px">
      <p class="copy" style="width:140px">Your skin is polished smooth and soft to the touch followed by a luxurious body cream massaged in to hydrate the newly revealed skin.</p>
      <div class="badge" style="right:8px;top:9px"><ul><li>Includes:</li><li>Body Scrub</li><li>Light Body Massage</li></ul></div>
    </div>
    <div class="photo" style="left:8px;right:8px;top:314px;height:156px;border-radius:0;background:linear-gradient(140deg,#f2e4dc,#d98a9a 45%,#7a3a20)" role="img" aria-label="Body scrub jar, serum bottle and brush"></div>
  </article>

  <article class="panel panel--pamper wood">
    <div class="photo" style="left:8px;right:8px;top:10px;height:110px;border-radius:0;background:linear-gradient(135deg,#f3eee8,#d9c4a8 55%,#9a5a30)" role="img" aria-label="Pampering products with towel and tubes"></div>
    <div class="band band--wood" style="top:126px">Pampering Body Treatment (1.5hrs)</div>
    <div class="box" style="top:148px;height:94px;padding:6px">
      <p class="copy" style="width:130px">An all over body treatment begins with a body scrub to exfoliate dead skin, in preparation for a body wrap that restores your skin to youthful condition. Lastly a luxurious body cream is massaged in leaving your skin beautifully radiant.</p>
      <div class="badge" style="right:8px;top:16px;width:62px;height:62px;padding-top:12px"><ul><li>Includes:</li><li>Body Scrub</li><li>Body Wrap with Head Massage</li><li>Light Body Massage</li></ul></div>
    </div>
    <div class="band band--wood" style="top:248px">Waxing</div>
    <div class="box" style="top:270px;bottom:10px">
      <p class="copy" style="position:absolute;left:6px;top:8px;width:92px;font-size:7px">We take care of all the unsightly hairy body parts, just leave it to us. Walk out like a new sexy you!</p>
      <div class="photo" style="right:0;top:0;width:120px;height:100px;border-radius:0;background:linear-gradient(150deg,#f6efe3,#e2b36a)" role="img" aria-label="Papaya body product tub"></div>
      <div class="photo" style="left:0;right:0;bottom:0;height:96px;border-radius:0;background:linear-gradient(120deg,#efe2d3,#d7a173 50%,#8a4a2a)" role="img" aria-label="Spa salts and body butter jars"></div>
    </div>
  </article>
</section>

</body>
</html>
```